Law Firm Logo and Business Card Design

I need a logo and business card design for a law firm I just started. The law firm is named Law Office of Doreen K. Ashworth, LLC. The type of law I practice is Family Law, which includes divorce, custody, child support, alimony, property division, and the like. I would like to see designs that are unique and modern, yet sophisticated. I would also like to use the logo/design for my letterhead. I am not opposed to using some form of the scales of justice although I'd like something other than the typical, old fashioned scales of justice. I had considered a house made out of puzzle pieces with one puzzle piece pulled away from the others, with the logo text reading "Putting your life back together, one piece at a time." However, I don't want that particular design to look juvenile. I also would not be opposed to some form of my initials on the logo -- my initials are DKA. I am open to any other ideas you may have. I would like to see raised designs/lettering, and/or metallic finish. I like the colors black, white, gold, silver, and/or teal.

Industry/Entity Type

Law Firm

```html
<!DOCTYPE html>
<html lang="en">
<head>
<meta charset="utf-8">
<title>Law Office of Doreen K. Ashworth, LLC — Business Card</title>
<link rel="stylesheet" href="https://fonts.googleapis.com/css2?family=Oswald:wght@500;600;700&display=swap">
<style>
  :root {
    --bg: #2a2623;
    --card-black: #0b0b0b;
    --card-black-hi: #1c1c1c;
    --gold: #f3c51c;
    --band-yellow: #ffd422;
    --band-amber: #f5b70f;
    --icon-red: #e0393a;
    --ink: #111111;
  }
  * { box-sizing: border-box; margin: 0; padding: 0; }
  html, body {
    width: 1200px; height: 900px; overflow: hidden;
    background: var(--bg);
    font-family: "Oswald", "Arial Narrow", sans-serif;
  }
  .canvas { position: relative; width: 1200px; height: 900px; }

  .card {
    position: absolute;
    width: 540px; height: 309px;
    border-radius: 18px;
    overflow: hidden;
    background: linear-gradient(150deg, var(--card-black-hi) 0%, var(--card-black) 45%, var(--card-black) 100%);
    box-shadow: 0 18px 40px rgba(0,0,0,.45);
  }
  .card-front { left: 40px; top: 296px; }
  .card-back  { left: 620px; top: 296px; }

  /* Front */
  .front-mark {
    position: absolute; left: 0; right: 0; top: 70px;
    display: flex; justify-content: center; align-items: center; gap: 16px;
  }
  .mark-square {
    width: 52px; height: 52px; border: 4px solid var(--gold);
  }
  .mark-initials {
    color: var(--gold); font-weight: 700; font-size: 72px; line-height: 1;
    letter-spacing: 4px;
  }
  .front-firm {
    position: absolute; left: 0; right: 0; top: 200px; text-align: center;
    color: var(--gold); font-weight: 600; font-size: 22px; letter-spacing: 1px;
    text-transform: uppercase;
  }

  /* Back */
  .attorney-name {
    position: absolute; left: 110px; top: 34px;
    color: var(--gold); font-weight: 700; font-size: 28px; letter-spacing: 1px;
    text-transform: uppercase; white-space: nowrap;
  }
  .back-mark {
    position: absolute; left: 30px; top: 120px;
    display: flex; align-items: center; gap: 10px;
  }
  .back-mark .mark-square { width: 30px; height: 30px; border-width: 3px; }
  .back-mark .mark-initials { font-size: 44px; letter-spacing: 2px; }
  .back-firm {
    position: absolute; left: 30px; top: 182px;
    color: var(--gold); font-weight: 500; font-size: 10px; letter-spacing: .4px;
    text-transform: uppercase; white-space: nowrap;
  }

  .contact-pole {
    position: absolute; left: 262px; top: 92px; width: 22px; height: 165px;
    background: repeating-linear-gradient(180deg, var(--band-yellow) 0 26px, var(--band-amber) 26px 30px);
  }
  .contact-list {
    position: absolute; left: 256px; top: 96px;
    list-style: none; display: flex; flex-direction: column; gap: 12px;
  }
  .contact-item { display: flex; align-items: center; gap: 10px; }
  .contact-icon {
    flex: none;
    width: 34px; height: 26px; background: var(--icon-red); border-radius: 3px;
    display: flex; align-items: center; justify-content: center;
  }
  .contact-text {
    color: var(--gold); font-weight: 500; font-size: 12.5px; letter-spacing: .3px;
    text-transform: uppercase; white-space: nowrap;
  }

  .address-band {
    position: absolute; left: 0; right: 0; bottom: 0; height: 52px;
    background: linear-gradient(90deg, var(--band-amber), var(--band-yellow) 60%);
    display: flex; align-items: center; justify-content: center;
    color: var(--ink); font-weight: 700; font-size: 19px; letter-spacing: .5px;
    text-transform: uppercase; white-space: nowrap;
  }
</style>
</head>
<body>
<main class="canvas">

  <section class="card card-front" aria-label="Card front">
    <div class="front-mark">
      <span class="mark-square"></span>
      <span class="mark-initials">DKA</span>
    </div>
    <p class="front-firm">Law Office of Doreen K. Ashworth, LLC</p>
  </section>

  <section class="card card-back" aria-label="Card back">
    <h1 class="attorney-name">Doreen K. Ashworth</h1>

    <div class="back-mark">
      <span class="mark-square"></span>
      <span class="mark-initials">DKA</span>
    </div>
    <p class="back-firm">Law Office of Doreen K. Ashworth, LLC</p>

    <div class="contact-pole"></div>
    <ul class="contact-list">
      <li class="contact-item">
        <span class="contact-icon">
          <svg width="16" height="16" viewBox="0 0 24 24" aria-hidden="true"><path fill="#fff" d="M6.6 10.8a15.1 15.1 0 0 0 6.6 6.6l2.2-2.2a1 1 0 0 1 1-.25 11.4 11.4 0 0 0 3.6.57 1 1 0 0 1 1 1V20a1 1 0 0 1-1 1A17 17 0 0 1 3 4a1 1 0 0 1 1-1h3.5a1 1 0 0 1 1 1c0 1.25.2 2.45.57 3.6a1 1 0 0 1-.25 1z"/></svg>
        </span>
        <span class="contact-text">410-555-0172</span>
      </li>
      <li class="contact-item">
        <span class="contact-icon">
          <svg width="18" height="14" viewBox="0 0 24 18" aria-hidden="true"><rect x="1" y="1" width="22" height="16" fill="none" stroke="#fff" stroke-width="2"/><path d="M1 1l11 9 11-9" fill="none" stroke="#fff" stroke-width="2"/></svg>
        </span>
        <span class="contact-text">doreen@ashworthfamilylaw.com</span>
      </li>
      <li class="contact-item">
        <span class="contact-icon">
          <svg width="16" height="16" viewBox="0 0 24 24" aria-hidden="true"><g fill="none" stroke="#fff" stroke-width="2"><circle cx="12" cy="12" r="10"/><ellipse cx="12" cy="12" rx="4.5" ry="10"/><path d="M2 12h20M4 6.5h16M4 17.5h16"/></g></svg>
        </span>
        <span class="contact-text">www.ashworthfamilylaw.com</span>
      </li>
    </ul>

    <div class="address-band">2214 Harbor Point Blvd. Suite 310 Easton, MD 21601</div>
  </section>

</main>
</body>
</html>
```